Flyer for Custom Home Builder!

my company is Harlow Ridge Homes, I am looking for a flyer that we can send via email to a customer, or print and hand out. I am thinking four pages so we could print this and fold it., possibly creating a folder. The name of the company is Harlow Ridge Homes our website is here www.harlowridgehomes-example.com. Some text you can use "Crafting luxury homes isn't just a job, it's our passion.
With meticulous attention to detail and an unwavering commitment to using the finest materials, Harlow Ridge Homes consistently delivers exceptional results that stand as a testament to our commitment to quality."

"Trust is the cornerstone of our foundation.
With a proven track record of delivering on our promises for over 16 years, we prioritize transparent communication and integrity throughout every step of the home-building journey".

you may need to obtain the photos here
https://files.example-share.net/f/k42pw7zm1rt8bq3xn6vya/h?key=93mfq2x8lw4tz6rb1kc7e&v=0

Target Market(s)

We build homes for every wealthy clients, therefore the photos are extremely important

Industry/Entity Type

Construction.

Requirements
Must have
• clear larger photos

```html
<!DOCTYPE html>
<html lang="en">
<head>
<meta charset="utf-8">
<title>Harlow Ridge Homes – Brochure Covers</title>
<link href="https://fonts.googleapis.com/css2?family=Cinzel:wght@400;600&family=Roboto:ital,wght@0,400;0,700;0,900;1,400&display=swap" rel="stylesheet">
<style>
  :root {
    --backdrop: #d3d2d3;
    --paper: #e4e2de;
    --slate: #b2b1b5;
    --ink: #111111;
    --charcoal: #2a2a2a;
    --white: #ffffff;
  }
  * { margin: 0; padding: 0; box-sizing: border-box; }
  html, body {
    width: 1200px; height: 840px; overflow: hidden;
    background: var(--backdrop);
    font-family: "Roboto", Arial, sans-serif;
    color: var(--ink);
  }
  .spread {
    position: absolute; left: 60px; top: 70px;
    width: 1080px; height: 700px;
    display: flex;
    box-shadow: 0 10px 30px rgba(0,0,0,0.18);
  }
  .page { position: relative; width: 540px; height: 700px; overflow: hidden; background: var(--paper); }
  .page-art { position: absolute; inset: 0; }

  /* back cover */
  .back-brand {
    position: absolute; left: 40px; top: 410px;
    font-weight: 900; font-size: 26px; letter-spacing: 2px;
    color: var(--charcoal); text-transform: uppercase;
  }
  .back-name {
    position: absolute; left: 40px; top: 458px;
    font-weight: 700; font-size: 19px; color: var(--ink);
  }
  .contact-list { position: absolute; left: 40px; top: 496px; list-style: none; }
  .contact-item {
    display: flex; align-items: center; gap: 10px;
    font-size: 12.5px; margin-bottom: 10px; color: var(--ink);
  }
  .contact-item.address { align-items: flex-start; line-height: 1.35; }
  .contact-item.web { font-weight: 700; }
  .contact-icon {
    flex: 0 0 24px; width: 24px; height: 24px;
    border: 1.4px solid var(--ink); border-radius: 50%;
    display: flex; align-items: center; justify-content: center;
  }

  /* front cover */
  .front-brand {
    position: absolute; right: 40px; top: 22px;
    font-weight: 900; font-size: 26px; letter-spacing: 2px;
    color: var(--charcoal); text-transform: uppercase;
  }
  .front-headline {
    position: absolute; left: 0; right: 0; top: 506px;
    text-align: center; color: var(--white);
    font-family: "Cinzel", "Times New Roman", serif;
  }
  .front-headline .title { font-size: 33px; font-weight: 600; letter-spacing: 2px; }
  .front-headline .subtitle { font-size: 17px; letter-spacing: 1.5px; margin-top: 6px; }
  .front-intro {
    position: absolute; left: 50px; right: 50px; top: 618px;
    text-align: center; font-weight: 700; font-size: 13.5px; line-height: 1.45;
  }
</style>
</head>
<body>
<main class="spread">

  <section class="page back-cover">
    <svg class="page-art" width="540" height="700" viewBox="0 0 540 700">
      <defs>
        <linearGradient id="duskEstate" x1="0" y1="0" x2="0" y2="1">
          <stop offset="0" stop-color="#3b2f4f"/>
          <stop offset="0.35" stop-color="#2c3350"/>
          <stop offset="0.7" stop-color="#2a2c33"/>
          <stop offset="1" stop-color="#1d1f22"/>
        </linearGradient>
      </defs>
      <rect width="540" height="700" fill="var(--paper)"/>
      <path d="M380,560 Q420,548 540,545 V700 H330 Z" fill="var(--slate)"/>
      <g role="img" aria-label="Photo of a stucco estate home with a tiled roof and lit windows at dusk">
        <path d="M0,0 H540 V470 L395,470 Q382,472 380,485 L376,560 L372,380 L0,380 Z" fill="url(#duskEstate)"/>
      </g>
      <g class="accent-stripes" fill="var(--ink)">
        <polygon points="400,486 540,476 540,496 392,506"/>
        <polygon points="392,514 540,504 540,522 386,534"/>
        <polygon points="386,542 540,530 540,548 382,560"/>
      </g>
    </svg>

    <div class="back-brand">Harlow Ridge Homes</div>
    <div class="back-name">Harlow Ridge Homes</div>
    <ul class="contact-list">
      <li class="contact-item">
        <span class="contact-icon"><svg width="12" height="12" viewBox="0 0 24 24"><path d="M6.6 10.8a15 15 0 0 0 6.6 6.6l2.2-2.2a1 1 0 0 1 1-.25 11.4 11.4 0 0 0 3.6.57 1 1 0 0 1 1 1V20a1 1 0 0 1-1 1A17 17 0 0 1 3 4a1 1 0 0 1 1-1h3.5a1 1 0 0 1 1 1c0 1.25.2 2.45.57 3.57a1 1 0 0 1-.25 1z" fill="none" stroke="currentColor" stroke-width="2"/></svg></span>
        (555) 014-2286
      </li>
      <li class="contact-item">
        <span class="contact-icon"><svg width="12" height="12" viewBox="0 0 24 24"><rect x="2" y="5" width="20" height="14" fill="none" stroke="currentColor" stroke-width="2"/><path d="M2 5l10 8 10-8" fill="none" stroke="currentColor" stroke-width="2"/></svg></span>
        HELLO@HARLOWRIDGE-EXAMPLE.COM
      </li>
      <li class="contact-item web">
        <span class="contact-icon"><svg width="12" height="12" viewBox="0 0 24 24"><circle cx="12" cy="12" r="9" fill="none" stroke="currentColor" stroke-width="2"/><path d="M3 12h18M12 3c3 3 3 15 0 18M12 3c-3 3-3 15 0 18" fill="none" stroke="currentColor" stroke-width="2"/></svg></span>
        www.harlowridgehomes-example.com
      </li>
      <li class="contact-item address">
        <span class="contact-icon"><svg width="12" height="12" viewBox="0 0 24 24"><path d="M12 22s7-7 7-12a7 7 0 0 0-14 0c0 5 7 12 7 12z" fill="none" stroke="currentColor" stroke-width="2"/><circle cx="12" cy="10" r="2.5" fill="none" stroke="currentColor" stroke-width="2"/></svg></span>
        <span>480 CEDAR BEND ROAD,<br>SUITE 210, FAIRHAVEN TX 78999</span>
      </li>
    </ul>
  </section>

  <section class="page front-cover">
    <svg class="page-art" width="540" height="700" viewBox="0 0 540 700">
      <defs>
        <linearGradient id="twilightResidence" x1="0" y1="0" x2="0" y2="1">
          <stop offset="0" stop-color="#c46cb4"/>
          <stop offset="0.3" stop-color="#a27a9c"/>
          <stop offset="0.6" stop-color="#8b7562"/>
          <stop offset="1" stop-color="#4e4640"/>
        </linearGradient>
      </defs>
      <rect width="540" height="700" fill="var(--paper)"/>
      <path d="M0,560 Q270,585 540,600 V700 H0 Z" fill="var(--slate)"/>
      <g role="img" aria-label="Photo of a modern two-storey stone and stucco luxury home with glowing windows under a pink twilight sky">
        <path d="M20,80 H540 V480 Q270,488 0,470 V110 Z" fill="url(#twilightResidence)"/>
      </g>
      <path d="M0,478 Q270,496 540,488 V598 Q270,582 0,560 Z" fill="var(--ink)"/>
      <path d="M0,474 Q270,492 540,484" fill="none" stroke="var(--paper)" stroke-width="4"/>
    </svg>

    <div class="front-brand">Harlow Ridge Homes</div>
    <div class="front-headline">
      <div class="title">CRAFTING LUXURY HOMES</div>
      <div class="subtitle">ISN'T JUST A JOB, IT'S OUR PASSION.</div>
    </div>
    <p class="front-intro">With meticulous attention to detail and an unwavering commitment to using the finest materials, Harlow Ridge Homes consistently delivers exceptional results that stand as a testament to our commitment to quality.</p>
  </section>

</main>
</body>
</html>
```